Dorrie's Letterhead

Letterhead should say: Dorrie Fenwick Childern's Book Author/Illustrator

Font should be fun and colorful, but not so distracting that it over shadows the letters content. My business card is shaped like a bone so I would like to keep that shape somewhere in the theme of the letterhead. You can find my book on Bookvale Wiggo and the Silver Kite if you would like to get a sense of my artistic style.
Updates

While I did say I want to carry out the bone theme. Don't be afraid to expand on that example: book shaped like a bone, paint brush...really go for it.

Surprise me! Good luck

Target Market(s)

Adults buying my book

Industry/Entity Type

Business

Requirements
Must have
• Fun colorful
Should not have
• Only one color

```html
<!DOCTYPE html>
<html lang="en">
<head>
<meta charset="utf-8">
<title>Dorrie Fenwick – Letterhead</title>
<link rel="stylesheet" href="https://fonts.googleapis.com/css2?family=Fredoka:wght@600&family=Open+Sans:wght@400;700&family=Raleway:wght@400&family=Comic+Neue:wght@400&display=swap">
<style>
  :root {
    --backdrop: #e9e9e9;
    --sheet-edge: #ffffff;
    --sheet-fill: #dce7ee;
    --cloud: #f6f7f8;
    --ink: #3d3d3d;
    --ink-soft: #4a4a4a;
    --name: #3a78c9;
    --tagline: #ef7f2b;
    --line-faint: #c4d2dd;
    --dot-line: #9cc8d4;
    --art-blue: #b9d6ea;
    --art-teal: #bfe0df;
    --art-red: #efc3c6;
    --art-pink: #ecd0df;
    --art-green: #d3e6c6;
    --art-violet: #d8cfe4;
    --art-sign: #cfdbe4;
  }
  * { box-sizing: border-box; margin: 0; padding: 0; }
  html, body { width: 1200px; height: 1000px; overflow: hidden; }
  body { background: var(--backdrop); position: relative; font-family: "Open Sans", sans-serif; }

  .sheet {
    position: absolute; left: 266px; top: 29px;
    width: 667px; height: 942px;
    background: var(--sheet-edge);
    padding: 22px;
  }
  .sheet__panel {
    position: relative; width: 623px; height: 898px;
    background: var(--sheet-fill); overflow: hidden;
  }
  .sheet__decor { position: absolute; inset: 0; }

  .art { position: absolute; border-radius: 40%; }
  .art--bone { left: 129px; top: 62px; width: 75px; height: 58px; background: var(--art-blue); border-radius: 30px; opacity: .7; }
  .art--bird { left: 330px; top: 72px; width: 59px; height: 39px; background: var(--art-teal); }
  .art--butterfly { left: 48px; top: 645px; width: 50px; height: 42px; background: var(--art-red); }
  .art--flower-blue { left: 393px; top: 706px; width: 39px; height: 39px; background: var(--art-blue); border-radius: 50%; }
  .art--flower-lime { left: 542px; top: 741px; width: 33px; height: 31px; background: var(--art-green); border-radius: 50%; }
  .art--flower-green { left: 29px; top: 764px; width: 42px; height: 39px; background: var(--art-green); border-radius: 50%; }
  .art--flower-pink { left: 195px; top: 758px; width: 33px; height: 33px; background: var(--art-pink); border-radius: 50%; }
  .art--chick-violet { left: 325px; top: 767px; width: 42px; height: 56px; background: var(--art-violet); }
  .art--bird-red { left: 481px; top: 814px; width: 46px; height: 39px; background: var(--art-red); }
  .art--chick-blue { left: 100px; top: 842px; width: 34px; height: 39px; background: var(--art-blue); }
  .art--signature { left: 81px; top: 684px; width: 156px; height: 26px; background: var(--art-sign); border-radius: 13px; }

  .masthead { position: absolute; right: 37px; top: 30px; text-align: right; }
  .masthead__name {
    font-family: "Fredoka", sans-serif; font-weight: 600;
    font-size: 27px; line-height: 1; color: var(--name); letter-spacing: .3px;
  }
  .masthead__role {
    font-family: "Comic Neue", sans-serif; font-size: 13px;
    color: var(--tagline); margin-top: 6px;
  }

  .recipient {
    position: absolute; left: 47px; top: 206px;
    font-size: 12px; line-height: 16.5px; color: var(--ink-soft);
  }
  .recipient strong { color: #2e2e2e; font-weight: 700; }

  .letter-body {
    position: absolute; left: 47px; top: 297px; width: 558px;
    font-size: 11.9px; line-height: 16px; color: var(--ink);
    text-align: justify;
  }
  .letter-body p + p { margin-top: 16px; }

  .sign-off__caption {
    position: absolute; left: 81px; top: 714px;
    font-size: 8px; color: var(--ink);
  }

  .contact {
    position: absolute; top: 868px; left: 146px;
    font-family: "Raleway", sans-serif; font-size: 12px; color: var(--ink-soft);
    display: flex; gap: 32px;
  }
</style>
</head>
<body>
  <main class="sheet">
    <div class="sheet__panel">
      <svg class="sheet__decor" width="623" height="898" viewBox="0 0 623 898" aria-hidden="true">
        <g fill="var(--cloud)">
          <circle cx="55" cy="40" r="96"/>
          <circle cx="130" cy="-5" r="62"/>
          <rect x="0" y="0" width="60" height="60"/>
        </g>
        <path class="dot-trail" d="M392 95 C 440 125, 540 135, 623 118" fill="none" stroke="var(--dot-line)" stroke-width="1.2" stroke-dasharray="3 3"/>
        <path d="M70 690 C 80 760, 150 800, 240 830 S 330 880, 360 898" fill="none" stroke="var(--line-faint)" stroke-width="1"/>
        <path d="M300 800 C 380 750, 520 740, 623 790" fill="none" stroke="var(--line-faint)" stroke-width="1"/>
      </svg>

      <div class="art art--bone" role="img" aria-label="Line drawing of a dog bone"></div>
      <div class="art art--bird" role="img" aria-label="Line drawing of a small flying bird"></div>

      <header class="masthead">
        <h1 class="masthead__name">Dorrie Fenwick</h1>
        <p class="masthead__role">Children's book Author/Illustrator</p>
      </header>

      <address class="recipient" style="font-style: normal;">
        <strong>Lorem ipsum</strong><br>
        Dolor sit amet<br>
        ei eros vidit sonet<br>
        sed
      </address>

      <section class="letter-body">
        <p>Lorem ipsum dolor sit amet, ei eros vidit sonet eum, sed ea aliquam offendit. Reque quando labitur nec in, no solum ceteros est. Accumsan pertinacia an qui. Te vidisse recteque pro, cu per habemus officiis, eos ex malis posidonium omittantur. Appetere principes eloquentiam vis ei, an mea alia petentium dignissim, te justo omnium duo.</p>
        <p>Movet laoreet delicatissimi cum id. Essent dissentiet cu cum, atqui augue iriure qui ea. Liber propriae ei sed. Euismod ornatus scaevola et pro.</p>
        <p>Verterem interesset disputationi vim et, laudem persecuti quo eu. Mea viderer vulputate ut. Ad scripta scaevola appetere usu, omnium forensibus sed cu, dolorum admodum postulant mea ei. Eos ut ubique graeco insolens, etiam electram assentior cum at.</p>
        <p>In eos solum verterem facilisis, magna scaevola explicari has ex, at vidisse percipitur cum. At dicam postea luptatum sea, sed te timeam principes disputando, postea scaevola eloquentiam quo eu. Cetero concludaturque cu ius, nam erat detraxit ut, in his cetero vocent erroribus. Eu sint nulla comprehensam qui. Dolor dolorum splendide ei est, id usu inani liber deterruisset.</p>
        <p>Omnis intellegat intellegam duo cu, no ornatus partiendo referrentur has</p>
      </section>

      <div class="art art--butterfly" role="img" aria-label="Line drawing of a butterfly"></div>
      <div class="art art--signature" role="img" aria-label="Handwritten signature of Dorrie Fenwick"></div>
      <p class="sign-off__caption">Dorrie Fenwick, Children's book Author/Illustrator</p>

      <div class="art art--flower-blue" role="img" aria-label="Line drawing of a blue flower"></div>
      <div class="art art--flower-lime" role="img" aria-label="Line drawing of a green flower"></div>
      <div class="art art--flower-green" role="img" aria-label="Line drawing of a green daisy"></div>
      <div class="art art--flower-pink" role="img" aria-label="Line drawing of a pink flower"></div>
      <div class="art art--chick-violet" role="img" aria-label="Line drawing of a small chick"></div>
      <div class="art art--bird-red" role="img" aria-label="Line drawing of a little bird"></div>
      <div class="art art--chick-blue" role="img" aria-label="Line drawing of a small blue chick"></div>

      <footer class="contact">
        <span class="contact__phone">Cell: (555) 204-7718</span>
        <span class="contact__email">Email: wiggoskite@mailvale.net</span>
      </footer>
    </div>
  </main>
</body>
</html>
```